Business Card design for a company called Tallow Flame NI

I need a business card design for my oil fired boiler servicing company. I have a logo design already and Im just looking that incorporated into the business card design. card details; Tallow Flame NI
Oil Burner Servicing - Mid Ulster Area
Service Engineer - Owen Marsh
Mobile 07751364927
email - Tallow.Flame.NI@hearthmail.example
www.tallowflameni.example
I carry out Servicing, Commissioning, Fault Finding, Warranty Validation
Target Market(s)
home owners with oil fired central heating
Industry/Entity Type
Business
Contact Information for Business Card
Tallow Flame NI
Tell. 07751364927
Web: www.tallowflameni.example
email Tallow.Flame.NI@Hearthmail.Example
Servicing Fault Finding Commissioning Warranty Validation
Look and feel

```html
<!DOCTYPE html>
<html lang="en">
<head>
<meta charset="utf-8">
<title>Tallow Flame NI – Business Card</title>
<link rel="stylesheet" href="https://fonts.googleapis.com/css2?family=Open+Sans:wght@400;600;700&display=swap">
<style>
  :root {
    --stage: #2a2a2a;
    --card: #ffffff;
    --green: #62bb46;
    --white: #ffffff;
  }
  * { box-sizing: border-box; margin: 0; padding: 0; }
  html, body {
    width: 1200px; height: 900px; overflow: hidden;
    background: var(--stage);
    font-family: "Open Sans", Arial, sans-serif;
  }
  .stage {
    width: 1200px; height: 900px;
    display: flex; align-items: center; justify-content: center;
  }
  .business-card {
    position: relative;
    width: 1000px; height: 572px;
    background: var(--card);
    border-radius: 34px;
    overflow: hidden;
  }
  .card-shapes { position: absolute; inset: 0; }

  .brand {
    position: absolute; left: 70px; top: 52px;
    display: flex; align-items: center; gap: 22px;
  }
  .brand-dot {
    width: 96px; height: 96px; border-radius: 50%;
    background: var(--green);
  }
  .brand-name {
    font-size: 60px; font-weight: 700; line-height: 1;
    color: var(--green);
    white-space: nowrap;
  }
  .brand-tagline {
    margin-top: 8px;
    font-size: 15px; font-weight: 600; letter-spacing: 4px;
    color: var(--green);
    white-space: nowrap;
  }

  .engineer {
    position: absolute; left: 72px; top: 372px;
    color: var(--white);
  }
  .engineer-name { font-size: 32px; font-weight: 700; line-height: 1.1; white-space: nowrap; }
  .engineer-role { font-size: 18px; padding-left: 12px; white-space: nowrap; }

  .contact-list {
    position: absolute; right: 50px; top: 248px;
    list-style: none;
    display: flex; flex-direction: column; gap: 12px;
    color: var(--white);
  }
  .contact-item {
    display: flex; align-items: center; justify-content: flex-end; gap: 14px;
    font-size: 19px;
    white-space: nowrap;
  }
  .contact-icon {
    flex: none;
    width: 40px; height: 34px; border-radius: 6px;
    background: var(--white);
    display: flex; align-items: center; justify-content: center;
  }
  .contact-icon svg { width: 24px; height: 24px; }

  .services {
    position: absolute; left: 0; right: 0; top: 492px;
    display: flex; align-items: center; justify-content: center; gap: 22px;
    color: var(--green);
    font-size: 23px;
    white-space: nowrap;
  }
  .services-rule { flex: none; width: 90px; height: 2px; background: var(--green); }
  .services-sep { font-size: 14px; margin: 0 6px; vertical-align: middle; }
</style>
</head>
<body>
<main class="stage">
  <article class="business-card">
    <svg class="card-shapes" viewBox="0 0 1000 572" aria-hidden="true">
      <path d="M0 300 H400 V220 H1000 V470 H0 Z" fill="var(--green)"/>
      <circle cx="400" cy="300" r="118" fill="var(--card)"/>
    </svg>

    <header class="brand">
      <span class="brand-dot" aria-hidden="true"></span>
      <div>
        <h1 class="brand-name">Tallow Flame NI</h1>
        <p class="brand-tagline">OIL BURNER SERVICING - MID ULSTER AREA</p>
      </div>
    </header>

    <div class="engineer">
      <p class="engineer-name">Owen Marsh</p>
      <p class="engineer-role">Service Engineer</p>
    </div>

    <ul class="contact-list">
      <li class="contact-item">07751364927
        <span class="contact-icon">
          <svg viewBox="0 0 24 24"><path d="M6.6 10.8a15 15 0 0 0 6.6 6.6l2.2-2.2c.3-.3.7-.4 1-.2 1.1.4 2.3.6 3.6.6.6 0 1 .4 1 1V20c0 .6-.4 1-1 1A17 17 0 0 1 3 4c0-.6.4-1 1-1h3.5c.6 0 1 .4 1 1 0 1.3.2 2.5.6 3.6.1.3 0 .7-.2 1z" fill="var(--green)"/></svg>
        </span>
      </li>
      <li class="contact-item">Tallow.Flame.NI@Hearthmail.Example
        <span class="contact-icon">
          <svg viewBox="0 0 24 24" fill="none" stroke="var(--green)" stroke-width="1.8"><rect x="2.5" y="5" width="19" height="14"/><path d="M2.5 5l9.5 8 9.5-8M2.5 19l7-6.5M21.5 19l-7-6.5"/></svg>
        </span>
      </li>
      <li class="contact-item">www.tallowflameni.example
        <span class="contact-icon">
          <svg viewBox="0 0 24 24" fill="none" stroke="var(--green)" stroke-width="1.6"><circle cx="12" cy="12" r="9"/><ellipse cx="12" cy="12" rx="4" ry="9"/><path d="M3 12h18M4.5 7.5h15M4.5 16.5h15"/></svg>
        </span>
      </li>
    </ul>

    <footer class="services">
      <span class="services-rule"></span>
      <p>Servicing <span class="services-sep">●</span> Fault Finding <span class="services-sep">●</span> Commissioning <span class="services-sep">●</span> Warranty Validation</p>
      <span class="services-rule"></span>
    </footer>
  </article>
</main>
</body>
</html>
```